2023 GLR Festival Form

• We are looking for a one-page form front and back. Something that comes that way, and we don’t have to merge it.
• Must be a fillable form, PDF version.
• The form will need to be editable; we will make minor changes as needed to the form, mainly contact information.
• Please add pictures, descriptions, and a registration area that includes a grand total donated.
• Attached are descriptions, links, and additional information that may help you develop a fluid registration form for us.

```html
<!DOCTYPE html>
<html lang="en">
<head>
<meta charset="utf-8">
<title>GLR Festival Registration Form</title>
<link href="https://fonts.googleapis.com/css2?family=Poppins:wght@300;400;500;600;700;800&family=Oswald:wght@500&display=swap" rel="stylesheet">
<style>
:root{
  --ink-dark:#241d1a;
  --ink-brown:#4a3328;
  --royal:#32319b;
  --sky:#aac0e2;
  --sky-pale:#d6e0f0;
  --gold:#f4df58;
  --field:#e5e5e5;
  --text:#2b2b2b;
  --canvas:#e9eaec;
  --paper:#ffffff;
}
*{box-sizing:border-box;margin:0;padding:0}
html,body{width:789px;height:1200px;overflow:hidden}
body{background:var(--canvas);font-family:"Poppins",sans-serif;color:var(--text);position:relative}
.page-slot{position:absolute;left:170px;width:448px;height:580px}
.page-slot.front{top:13px}
.page-slot.back{top:607px}
.page{position:absolute;top:0;left:0;width:676px;height:875px;background:var(--paper);transform:scale(.6629);transform-origin:0 0;overflow:hidden;box-shadow:0 4px 14px rgba(0,0,0,.18)}
.a{position:absolute}
.header-photo{position:absolute;left:0;top:0;width:676px;background:linear-gradient(100deg,var(--ink-dark) 0%,#2e2420 45%,var(--ink-brown) 75%,#3a2a22 100%)}
.title{font-weight:800;color:#fff;line-height:1;letter-spacing:.5px}
.title .ordinal{color:var(--gold)}
.title sup{font-size:.55em;vertical-align:.7em}
.date-band{background:var(--royal);color:var(--gold);font-weight:800;font-size:33px;letter-spacing:.5px;padding:6px 12px;line-height:1}
.location{color:#fff;font-size:14px;font-weight:400;letter-spacing:.3px}
.brand-name{color:#fff;font-weight:700;line-height:1.05;text-align:center}
.label{font-size:11px;line-height:1.2}
.field{position:absolute;background:var(--field);height:24px}
.box{display:inline-block;width:12px;height:12px;background:#dcdcdc;vertical-align:middle;margin-right:6px}
.check-label{font-size:11px;display:inline-flex;align-items:center}
.sponsor-panel{background:var(--royal)}
.tier{position:absolute;width:146px;height:22px;display:flex;align-items:center;padding-left:4px;font-size:10px;line-height:1;color:#333}
.tier .box{width:16px;height:16px;background:#eee;margin-right:8px}
.tier.diamond{background:linear-gradient(90deg,#fff,#e7e7e7 60%,#fafafa)}
.tier.golden{background:linear-gradient(90deg,#c79a1c,#f1d253 60%,#c69a22)}
.tier.silver{background:linear-gradient(90deg,#f2f2f2,#d3d3d3)}
.tier.bronze{background:linear-gradient(90deg,#8f5c2a,#c38d4d);color:#fff}
.tier.friend{background:linear-gradient(90deg,#c7d5ec,#f4f6fb)}
.tier b{font-weight:600}
.sponsorship-heading{font-family:"Oswald",sans-serif;font-weight:500;font-size:19px;line-height:1.05;color:#222}
.accent{color:var(--royal);font-weight:600}
.deadline{display:flex;height:26px}
.deadline .left{background:var(--royal);color:#fff;font-size:15px;width:347px;padding-left:46px;display:flex;align-items:center}
.deadline .right{background:var(--sky);color:#111;font-weight:700;font-size:15px;width:276px;display:flex;align-items:center;justify-content:center}
.agenda-bar{background:var(--royal);color:#fff;font-size:16px;padding-left:10px;display:flex;align-items:center}
.agenda-row{position:absolute;left:25px;width:352px;height:17px;display:flex;font-size:11px;background:linear-gradient(90deg,#fff,#f0f0f0)}
.agenda-row .time{width:118px;background:var(--sky);padding-left:8px;display:flex;align-items:center}
.agenda-row .what{padding-left:14px;display:flex;align-items:center}
.venue-photo{background:linear-gradient(180deg,#bfd3e6 0%,#e3e3df 30%,#9b4a34 55%,#6e6a5f 80%,#8a8a7e 100%)}
.icon{display:inline-block;vertical-align:middle}
/* back page */
.bar{background:var(--royal);color:#fff;text-align:center;font-size:12px;line-height:16px;height:16px}
.info-row{background:var(--field);display:flex;align-items:center;padding-left:8px;font-size:13px}
.tick-note{font-size:8.5px;line-height:1.2;display:flex;gap:4px}
.day{font-weight:700;font-size:11px}
.item-tag{height:14px;font-size:8.5px;line-height:14px;padding-left:8px;background:linear-gradient(90deg,var(--sky),var(--sky) 85%,#e6e6e6 85%)}
.price{height:14px;display:flex;font-size:8.5px;line-height:14px}
.price .what{background:var(--sky);padding-left:8px;width:87px}
.price .cost{background:var(--royal);color:#fff;width:28px;text-align:center}
.mini{font-size:8.5px;line-height:1.2}
.tag{height:14px;font-size:7.5px;line-height:14px;padding:0 6px;display:inline-block}
.tag.dark{background:var(--royal);color:#fff}
.tag.pale{background:var(--sky)}
.divider{position:absolute;left:27px;width:623px;height:1px;background:#cfcfcf}
.link{color:var(--royal)}
.sponsor-band{background:var(--royal)}
.sponsor-tab{background:var(--sky);color:var(--ink-dark);font-weight:700;font-size:18px;text-align:center;line-height:24px;clip-path:polygon(4% 0,96% 0,100% 100%,0 100%)}
.sponsor-name{color:#fff;font-weight:600;font-size:15px}
</style>
</head>
<body>

<div class="page-slot front">
<section class="page" aria-label="Festival registration form, front">
  <div class="header-photo" style="height:212px" role="img" aria-label="Dark photograph of hens behind the festival title"></div>
  <h1 class="title a" style="left:36px;top:26px;font-size:52px"><span class="ordinal">25<sup>TH</sup></span> ANNUAL<br>GLR FESTIVAL</h1>
  <div class="date-band a" style="left:25px;top:125px;width:386px">OCTOBER 6TH &amp; 7TH</div>
  <div class="location a" style="left:36px;top:182px">
    <svg class="icon" width="12" height="12" viewBox="0 0 12 12"><circle cx="6" cy="4" r="2.5" fill="none" stroke="#fff" stroke-width="1.3"/><path d="M2 11c.5-2.5 2-3.5 4-3.5s3.5 1 4 3.5" fill="none" stroke="#fff" stroke-width="1.3"/></svg>
    FAIRHAVEN, OH AT THE HARBORVIEW GRAND</div>
  <div class="brand-name a" style="left:430px;top:120px;width:226px;font-size:30px">Great Lakes<br><span style="font-size:17px">Ranchers</span></div>

  <div class="label a" style="left:35px;top:230px">Name of company</div>
  <div class="field" style="left:171px;top:225px;width:477px"></div>
  <div class="label a" style="left:35px;top:260px">Name of the contact<br>person</div>
  <div class="field" style="left:171px;top:257px;width:477px"></div>
  <div class="label a" style="left:35px;top:296px">Are you attending?</div>
  <div class="a" style="left:171px;top:292px;display:flex;gap:0">
    <span class="check-label" style="width:196px"><span class="box"></span>will not be attending</span>
    <span class="check-label" style="width:160px"><span class="box"></span>donation only</span>
    <span class="check-label"><span class="box"></span>donation for</span>
  </div>
  <div class="label a" style="left:35px;top:322px">Names of those who<br>are attending</div>
  <div class="field" style="left:171px;top:320px;width:154px"></div>
  <div class="field" style="left:334px;top:320px;width:154px"></div>
  <div class="field" style="left:497px;top:320px;width:151px"></div>
  <div class="a mini" style="left:171px;top:352px;font-size:10px">*Fill out only for those planning to attend 4 sports</div>
  <div class="label a" style="left:35px;top:373px">Email address of the<br>contact person</div>
  <div class="field" style="left:171px;top:370px;width:477px"></div>
  <div class="a" style="left:171px;top:402px;display:flex;gap:10px">
    <span class="check-label"><span class="box"></span>Golf</span>
    <span class="check-label"><span class="box"></span>Spa</span>
    <span class="check-label"><span class="box"></span>Bluegate</span>
    <span class="check-label"><span class="box"></span>Sporting Clay</span>
    <span class="check-label"><span class="box"></span>Banquet</span>
  </div>

  <svg class="a" style="left:65px;top:434px" width="34" height="34" viewBox="0 0 34 34"><circle cx="17" cy="17" r="16" fill="var(--royal)"/><circle cx="17" cy="13" r="6" fill="none" stroke="#fff" stroke-width="1.6"/><path d="M8 24l5-3h6l5 3" fill="none" stroke="#fff" stroke-width="1.6"/></svg>
  <div class="sponsorship-heading a" style="left:38px;top:478px">SPONSORSHIPS<br>LEVELS</div>
  <div class="sponsor-panel a" style="left:162px;top:428px;width:487px;height:112px"></div>
  <div class="tier diamond" style="left:171px;top:445px"><span class="box"></span><span>Diamond Sponsor<br><b>$5,000</b></span></div>
  <div class="tier golden" style="left:330px;top:445px"><span class="box"></span><span>Golden Egg Sponsor<br><b>$3,000</b></span></div>
  <div class="tier silver" style="left:490px;top:445px"><span class="box"></span><span>Silver Chicken Sponsor<br><b>$2,000</b></span></div>
  <div class="tier bronze" style="left:171px;top:480px"><span class="box"></span><span>Bronze Turkey Sponsor<br><b>$1,000</b></span></div>
  <div class="tier friend" style="left:330px;top:480px"><span class="box"></span><span>Friend of GLR<br><b>$500</b></span></div>
  <div class="a" style="left:171px;top:513px;color:var(--gold);font-size:11px;font-weight:500">The GLR is a nonprofit organization, and your donations are tax-deductible</div>

  <div class="a" style="left:35px;top:546px;font-size:14px;display:flex;align-items:center;gap:6px">
    <span style="font-size:9px">For more information contact</span>
    <span class="accent">Dana Whitlow</span>
    <svg class="icon" width="12" height="12" viewBox="0 0 12 12" style="margin-left:8px"><path d="M2 1.5l2.5 0 1 2.5-1.5 1a6 6 0 003 3l1-1.5 2.5 1v2.5c-5 .5-9-3.5-8.5-8.5z" fill="none" stroke="var(--royal)" stroke-width="1.2"/></svg>
    <span>555-404-2270</span>
    <svg class="icon" width="14" height="12" viewBox="0 0 14 12" style="margin-left:10px"><rect x="1" y="2" width="12" height="9" fill="none" stroke="var(--royal)" stroke-width="1.3"/><path d="M1 2l6 5 6-5" fill="none" stroke="var(--royal)" stroke-width="1.3"/></svg>
    <span>dwhitlow@glranchers.org</span>
  </div>
  <div class="deadline a" style="left:27px;top:573px"><div class="left">DEADLINE FOR REGISTRATION</div><div class="right">SEPTEMBER 15, 2022</div></div>

  <div class="a" style="left:35px;top:610px;font-size:12px;line-height:1.4">Make checks payable to the <span class="accent" style="font-size:15px">Great Lakes Ranchers</span> or pay via credit card<br>using the <span class="accent" style="font-size:15px">Registration form.</span></div>
  <div class="a" style="left:35px;top:659px;font-size:12px;line-height:1.35">Email Registration Forms to<br>
    <svg class="icon" width="14" height="12" viewBox="0 0 14 12"><rect x="1" y="2" width="12" height="9" fill="none" stroke="var(--royal)" stroke-width="1.3"/><path d="M1 2l6 5 6-5" fill="none" stroke="var(--royal)" stroke-width="1.3"/></svg>
    <span style="font-size:13px;margin-left:6px">dwhitlow@glranchers.org</span></div>
  <div class="a" style="left:304px;top:652px;font-size:12px;line-height:1.5">Mail payment and this registration form to<br>
    <svg class="icon" width="12" height="12" viewBox="0 0 12 12"><circle cx="6" cy="4" r="2.5" fill="none" stroke="var(--royal)" stroke-width="1.3"/><path d="M2 11c.5-2.5 2-3.5 4-3.5s3.5 1 4 3.5" fill="none" stroke="var(--royal)" stroke-width="1.3"/></svg>
    <span style="font-size:13px;margin-left:6px">1180 Orchard Station, Millbrook, OH 45011</span></div>

  <div class="agenda-bar a" style="left:25px;top:700px;width:623px;height:27px">Agenda</div>
  <div class="venue-photo a" style="left:377px;top:692px;width:272px;height:155px" role="img" aria-label="Photo of the hotel patio with umbrellas and brick walls"></div>
  <div class="agenda-row" style="top:737px"><div class="time">1:30 PM</div><div class="what">Set up Silent Auction</div></div>
  <div class="agenda-row" style="top:758px"><div class="time">4:30 PM</div><div class="what">Registration opens</div></div>
  <div class="agenda-row" style="top:779px"><div class="time">5:00 PM</div><div class="what">Silent auction, music, cash bar opens</div></div>
  <div class="agenda-row" style="top:802px"><div class="time">6:00 PM</div><div class="what">Annual Meeting &amp; Awards Banquet</div></div>
  <div class="agenda-row" style="top:823px"><div class="time">8:45 PM to 11:00 PM</div><div class="what">Moonlight Revue event</div></div>
</section>
</div>

<div class="page-slot back">
<section class="page" aria-label="Festival registration form, back">
  <div class="header-photo" style="height:92px" role="img" aria-label="Dark photograph of hens behind the festival title"></div>
  <h2 class="title a" style="left:45px;top:32px;font-size:33px"><span class="ordinal">25<sup>TH</sup></span> ANNUAL GLR FESTIVAL</h2>
  <div class="brand-name a" style="left:510px;top:38px;width:140px;font-size:14px">Great Lakes<br><span style="font-size:9px">Ranchers</span></div>

  <div class="bar a" style="left:36px;top:102px;width:604px">HOTEL INFORMATION</div>
  <div class="info-row a" style="left:35px;top:126px;width:610px;height:24px">Harborview Grand Golf Resort &amp; Spa</div>
  <div class="info-row a" style="left:35px;top:157px;width:610px;height:24px"><span style="font-size:11px;margin-right:12px">Dates</span><span class="link">October 6th and 7th</span>&nbsp;in Fairhaven, OH at the Harborview Grand</div>
  <div class="label a" style="left:35px;top:195px">Harbor Reservations</div>
  <div class="info-row a" style="left:163px;top:189px;width:482px;height:25px;font-size:14px">(800) 555-0142 or (555) 231-0190</div>
  <div class="tick-note a" style="left:146px;top:222px"><span>☑</span><span>Book by September 15th to make your room reservations.<br>Mention the Great Lakes Ranchers or GLR for your room block.</span></div>
  <div class="tick-note a" style="left:146px;top:252px"><span>☑</span></div>
  <div class="a" style="left:162px;top:248px;width:486px;height:34px;background:var(--sky);padding:6px 14px;font-size:8.5px;line-height:1.2;color:var(--ink-dark)">https://www.harborviewgrand.com/en-us/rooms/fairhaven-golf-resort-and-spa/overview/<br>?block=glr-festival-2023-room-block</div>

  <div class="bar a" style="left:26px;top:292px;width:624px">AGENDA</div>

  <div class="day a" style="left:35px;top:314px">FRIDAY</div>
  <div class="item-tag a" style="left:27px;top:329px;width:125px">Bluegate Tailgating</div>
  <div class="price a" style="left:178px;top:329px"><span class="what">Cost per person</span><span class="cost">$50</span></div>
  <div class="mini a" style="left:320px;top:331px">Email address of the person attending</div>
  <div class="field" style="left:495px;top:329px;width:155px;height:15px"></div>
  <div class="tick-note a" style="left:35px;top:349px"><span>☑</span><span>Complimentary Meal &amp; Bluegate<br>Grandstand Reserved Seating Included.</span></div>
  <div class="tick-note a" style="left:243px;top:349px"><span>☑</span><span>Food and fun 11:00 a.m.-1:00 p.m. EST</span></div>
  <div class="tick-note a" style="left:488px;top:349px"><span>☑</span><span>Races start at 1:05 p.m.</span></div>
  <div class="a" style="left:150px;top:380px;display:flex;align-items:center"><span class="mini" style="font-size:7.5px;margin-right:14px">SPONSORS</span><span class="tag dark">Northfield Animal Health Event sponsor</span><span class="tag pale">Local Beverages donated by Ridgeway Feeds</span></div>
  <div class="divider" style="top:401px"></div>

  <div class="day a" style="left:35px;top:406px">SATURDAY</div>
  <div class="item-tag a" style="left:27px;top:421px;width:125px">Golf</div>
  <div class="price a" style="left:178px;top:421px"><span class="what">Fees for scramble</span><span class="cost">$125</span></div>
  <div class="mini a" style="left:372px;top:419px">Email address of the<br>person attending</div>
  <div class="mini a" style="left:372px;top:443px">Average Score</div>
  <div class="field" style="left:495px;top:421px;width:155px;height:15px"></div>
  <div class="field" style="left:495px;top:441px;width:155px;height:15px"></div>
  <div class="mini a" style="left:35px;top:452px">The scramble will be held at<br>
    <span style="color:var(--royal)">●</span> Harborview Grand Golf Club, located at 1800 Meadow Pike, Fairhaven, OH<br>
    <span class="link">https://www.harborviewgolf.com/?block=glr-scramble-2023</span></div>
  <div class="mini a" style="left:47px;top:487px">Registration will begin Saturday, October 7th, at 7:45 AM ET,<br>and we will tee off at 8:30 AM. ET</div>
  <div class="mini a" style="left:357px;top:487px">lunch, Beverage cart drinks, and snacks are included</div>
  <div class="a" style="left:150px;top:515px;display:flex;align-items:center"><span class="mini" style="font-size:7.5px;margin-right:14px">SPONSORS</span><span class="tag dark">Millstone Pro – Golf Towel</span><span class="tag pale">Cedarline Labs – lunch</span><span class="tag dark">Brightside Design- drink cart</span></div>
  <div class="divider" style="top:537px"></div>

  <div class="item-tag a" style="left:27px;top:547px;width:125px">Spa</div>
  <div class="price a" style="left:205px;top:547px"><span class="what">Per person</span><span class="cost">$150</span></div>
  <div class="mini a" style="left:372px;top:549px">AM or PM Appointment?</div>
  <div class="a mini" style="left:495px;top:547px;display:flex;align-items:center"><span class="box"></span><span style="margin-right:12px">AM</span><span class="box"></span>PM</div>
  <div class="mini a" style="left:372px;top:566px">Phone no. of the person<br>with the appointment</div>
  <div class="field" style="left:495px;top:568px;width:155px;height:15px"></div>
  <div class="mini a link" style="left:35px;top:569px">https://thespaatharborview.com/</div>
  <div class="tick-note a" style="left:35px;top:581px"><span>☑</span><span>Limited appointments available</span></div>
  <div class="tick-note a" style="left:205px;top:581px"><span>☑</span><span>9:30 AM- 3:30 PM ET</span></div>
  <div class="divider" style="top:601px"></div>

  <div class="item-tag a" style="left:27px;top:615px;width:125px">Sporting clay</div>
  <div class="price a" style="left:205px;top:615px"><span class="what">Per person</span><span class="cost">$150</span></div>
  <div class="a" style="left:205px;top:632px;font-size:6px">Fees include food, drinks, snacks, &amp; ammo</div>
  <div class="mini a" style="left:372px;top:614px">Email address of the<br>person attending</div>
  <div class="mini a" style="left:372px;top:638px">Gauge size</div>
  <div class="field" style="left:495px;top:616px;width:155px;height:15px"></div>
  <div class="a mini" style="left:495px;top:637px;display:flex;align-items:center"><span class="box"></span><span style="margin-right:12px">20</span><span class="box"></span>12</div>
  <div class="tick-note a" style="left:35px;top:642px"><span>☑</span><span>Stag Hollow Hunting Club and Sporting Clay</span></div>
  <div class="mini a" style="left:35px;top:654px"><span style="color:var(--royal)">●</span> 1860 Ridge Road, Owensville, OH 45160 US<br>&nbsp;&nbsp;&nbsp;(55 Minutes from the hotel)</div>
  <div class="divider" style="top:684px"></div>

  <div class="item-tag a" style="left:27px;top:698px;width:125px">Banquet</div>
  <div class="price a" style="left:205px;top:698px"><span class="what">Per person</span><span class="cost">$150</span></div>
  <div class="mini a" style="left:372px;top:698px">Entertainment</div>
  <div class="a" style="left:495px;top:696px"><span class="box"></span></div>
  <div class="a" style="left:495px;top:716px"><span class="box"></span></div>
  <div class="mini a" style="left:518px;top:697px">Moonlight Revue</div>
  <div class="mini a" style="left:518px;top:712px">Join us for fun, games, music,<br>and around $3,000 in prizes!</div>
  <div class="tick-note a" style="left:35px;top:722px"><span>☑</span><span>Awards Banquet and Entertainment ticket</span></div>
  <div class="divider" style="top:743px"></div>

  <div class="item-tag a" style="left:27px;top:752px;width:183px">Static Trade Show Booth Requests</div>
  <div class="tick-note a" style="left:220px;top:754px"><span>☑</span><span>Trade Show Booth (6 ft table) $100</span></div>

  <div class="sponsor-band a" style="left:0;top:795px;width:676px;height:80px"></div>
  <div class="sponsor-tab a" style="left:205px;top:783px;width:260px;height:25px">OUR SPONSORS</div>
  <div class="sponsor-name a" style="left:58px;top:828px">Hartwell</div>
  <div class="sponsor-name a" style="left:230px;top:828px">Polar Freight</div>
  <div class="sponsor-name a" style="left:420px;top:828px">Veterix</div>
  <div class="sponsor-name a" style="left:575px;top:828px">Oakmere</div>
</section>
</div>

</body>
</html>
```